Wheels for Harborline Website Design

We need a NEW design and uploaded to Hostavero.com. Here is the current site: http://www.wheelsforharborline.org

Need a form like this:

https://brightlanegifts.org/

```html
<!DOCTYPE html>
<html lang="en">
<head>
<meta charset="utf-8">
<title>Wheels for Harborline — Car Donation Made Easy</title>
<link href="https://fonts.googleapis.com/css2?family=Fira+Sans:wght@400;500;600;700&display=swap" rel="stylesheet">
<style>
:root{
  --red:#c50f12;
  --navy:#0f1f66;
  --ink:#1f1f1f;
  --muted:#666;
  --line:#bdbdbd;
  --gray-band:#e6e4e4;
  --blue-a:#2c4fa8;
  --blue-b:#3a6bcf;
  --footer:#e9f3fb;
  --white:#fff;
}
*{box-sizing:border-box;margin:0;padding:0}
html,body{width:1200px;height:4189px;overflow:hidden}
body{position:relative;font-family:"Fira Sans",sans-serif;color:var(--ink);background:var(--white)}
.abs{position:absolute}
a{color:inherit;text-decoration:none}

/* header */
.site-header{left:0;top:0;width:1200px;height:114px;background:var(--white)}
.brand{left:110px;top:26px;display:flex;align-items:center;gap:10px;font-weight:700;font-size:26px;color:var(--red)}
.brand-dot{width:30px;height:30px;border-radius:50%;background:var(--red)}
.call-top{right:112px;top:14px;font-size:16px;display:flex;gap:14px;align-items:center}
.call-top strong{color:var(--red);font-weight:500}
.nav{left:400px;top:58px;display:flex;gap:34px;font-size:17px;font-weight:500}
.btn{display:inline-flex;align-items:center;justify-content:center;background:var(--red);color:var(--white);font-weight:600;border-radius:5px;text-transform:uppercase}
.btn-header{left:933px;top:47px;width:155px;height:47px;font-size:16px}

/* hero */
.hero{left:0;top:114px;width:1200px;height:556px;background:linear-gradient(100deg,#6d5a44 0%,#8a8467 30%,#5d7a3c 60%,#9aa66a 100%)}
.hero-text{right:112px;top:118px;text-align:right;color:var(--white)}
.hero-text h1{font-size:70px;font-weight:500;line-height:1}
.hero-text p{font-size:22px;margin-top:30px;font-weight:500}
.btn-hero{right:112px;top:442px;width:155px;height:46px;font-size:16px}

/* form card */
.form-card{left:110px;top:558px;width:978px;height:530px;background:var(--white);border-radius:6px;box-shadow:0 2px 12px rgba(0,0,0,.22)}
.steps{left:288px;top:46px;display:flex;align-items:center;font-size:17px}
.step-num{width:42px;height:42px;border-radius:50%;color:var(--white);display:flex;align-items:center;justify-content:center;font-size:20px;font-weight:500;margin-right:14px}
.step-1 .step-num{background:var(--navy)}
.step-1{color:var(--navy)}
.step-2 .step-num{background:#555}
.step-2{color:#444}
.step-line{width:84px;height:1px;background:#aaa;margin:0 18px}
.field{position:absolute;width:297px}
.field label{display:block;font-size:17px;font-weight:500;margin-bottom:10px}
.select{height:44px;border:1px solid var(--line);display:flex;align-items:center;justify-content:space-between;font-size:16px;color:#555;padding-left:8px}
.select i{width:48px;height:100%;border-left:1px solid var(--line);display:flex;align-items:center;justify-content:center}
.btn-donate{left:368px;top:331px;width:243px;height:55px;font-size:16px}
.badges{left:380px;top:420px;display:flex;gap:18px}
.badge{width:58px;height:58px;border-radius:50%}

/* how to donate */
.section-title{width:1200px;text-align:center;font-size:42px;font-weight:500}
.how-step{position:absolute;width:300px;text-align:center}
.how-icon{width:100px;height:90px;margin:0 auto;border-radius:8px;background:linear-gradient(135deg,#dbe0f2,#f3d7d7)}
.how-num{width:36px;height:36px;border:1px solid #555;border-radius:50%;margin:16px auto 10px;display:flex;align-items:center;justify-content:center;font-size:16px}
.how-step h3{font-size:17px;font-weight:600;margin-bottom:12px}
.how-step p{font-size:16px;color:var(--muted);line-height:26px}

/* impacts */
.impacts{left:0;top:1601px;width:1200px;height:659px;background:var(--gray-band)}
.impact-card{position:absolute;top:178px;width:309px;height:387px;background:var(--white);border-radius:6px;box-shadow:0 1px 6px rgba(0,0,0,.15);text-align:center;padding:10px}
.impact-photo{height:184px}
.impact-card h3{font-size:17px;font-weight:600;margin:32px 0 12px}
.impact-card p{font-size:15px;color:var(--muted);line-height:26px;padding:0 12px}
.impact-card a{display:block;margin-top:10px;color:var(--red);font-weight:600;font-size:16px}

/* why */
.why{left:0;top:2260px;width:1200px;height:595px;background:linear-gradient(180deg,var(--blue-a),var(--blue-b))}
.why-photo{left:620px;top:0;width:580px;height:595px;background:linear-gradient(160deg,#7d6e54,#b4a285 45%,#e7e3dc 70%,#8d7a5d)}
.why h2{left:110px;top:85px;color:var(--white);font-size:44px;font-weight:500}
.why-list{left:110px;top:168px;width:530px;list-style:none;color:var(--white);font-size:16px;line-height:26px}
.why-list li{padding-left:19px;position:relative;margin-bottom:25px}
.why-list li svg{position:absolute;left:0;top:6px}
.why-list b{font-weight:600}

/* faq */
.faq-item{position:absolute;left:190px;width:836px;border:1px solid #888;border-radius:5px;padding:0 48px 0 26px;display:flex;align-items:center;font-size:16px;font-weight:500;color:#333}
.faq-item svg{position:absolute;right:40px}
.faq-open{display:block;padding-top:28px}
.faq-open p{font-weight:400;color:#555;margin-top:22px;line-height:26px;width:680px}

/* footer */
.site-footer{left:0;top:3720px;width:1200px;height:469px;background:var(--footer)}
.foot-brand{left:116px;top:94px;display:flex;align-items:center;gap:10px;font-weight:700;font-size:26px;color:var(--red)}
.foot-about{left:112px;top:165px;width:380px;font-size:16px;line-height:26px;color:#444}
.foot-call{left:520px;top:94px;width:345px;text-align:center;font-size:16px}
.foot-call .phone{display:flex;align-items:center;justify-content:center;gap:10px;color:var(--red);font-size:34px;font-weight:600;margin:14px 0 8px}
.foot-seals{left:600px;top:230px;display:flex;gap:40px}
.seal-rect{width:104px;height:36px;background:#d9dde6;border-radius:4px}
.seal-circle{width:48px;height:48px;border-radius:50%;background:#6c9ad0}
.quick{left:938px;top:94px;font-size:16px}
.quick h4{font-weight:600;font-size:16px;margin-bottom:12px}
.quick a{display:block;margin-left:7px;color:#555;line-height:26px}
.foot-rule{left:112px;top:340px;width:976px;height:1px;background:#b9c4cd}
.copyright{left:112px;top:372px;font-size:16px;color:#444}
.socials{left:877px;top:358px;display:flex;gap:8px}
.social{width:48px;height:48px;border:1px solid var(--red);border-radius:50%}
</style>
</head>
<body>

<header class="site-header abs">
  <div class="brand abs"><span class="brand-dot"></span>Wheels for Harborline</div>
  <div class="call-top abs">
    <span>
      <svg width="14" height="14" viewBox="0 0 24 24" style="vertical-align:-2px"><path fill="#c50f12" d="M6.6 10.8a15 15 0 0 0 6.6 6.6l2.2-2.2c.3-.3.7-.4 1-.2 1.1.4 2.3.6 3.6.6.6 0 1 .4 1 1V20c0 .6-.4 1-1 1A17 17 0 0 1 3 4c0-.6.4-1 1-1h3.5c.6 0 1 .4 1 1 0 1.3.2 2.5.6 3.6.1.3 0 .7-.2 1z"/></svg>
      Call Today To Donate</span>
    <strong>1-888-555-0142</strong>
  </div>
  <nav class="nav abs"><a>About</a><a>How to Donate</a><a>Wy Donate</a><a>FAQs</a><a>Contact</a></nav>
  <a class="btn btn-header abs">Donate a car</a>
</header>

<section class="hero abs" role="img" aria-label="Photo of a soldier in camouflage hugging a young boy holding a flag, garden background">
  <div class="hero-text abs">
    <h1>Car Donation<br>Made Easy</h1>
    <p>Join Our 500,000+ donors</p>
  </div>
  <a class="btn btn-hero abs">Join us now !</a>
</section>

<form class="form-card abs">
  <div class="steps abs">
    <div class="step-1" style="display:flex;align-items:center"><span class="step-num">1</span>Vehicle info</div>
    <span class="step-line"></span>
    <div class="step-2" style="display:flex;align-items:center"><span class="step-num">2</span>Contact info</div>
  </div>
  <div class="field" style="left:31px;top:115px"><label>Year</label><div class="select">Select Year<i><svg width="12" height="8" viewBox="0 0 12 8"><path d="M1 1l5 5 5-5" fill="none" stroke="#555" stroke-width="1.4"/></svg></i></div></div>
  <div class="field" style="left:341px;top:115px"><label>Make</label><div class="select">Select Make<i><svg width="12" height="8" viewBox="0 0 12 8"><path d="M1 1l5 5 5-5" fill="none" stroke="#555" stroke-width="1.4"/></svg></i></div></div>
  <div class="field" style="left:651px;top:115px"><label>Model</label><div class="select">Select Model<i><svg width="12" height="8" viewBox="0 0 12 8"><path d="M1 1l5 5 5-5" fill="none" stroke="#555" stroke-width="1.4"/></svg></i></div></div>
  <div class="field" style="left:31px;top:218px"><label>Mileage</label><div class="select">Enter Mileage<i><svg width="12" height="8" viewBox="0 0 12 8"><path d="M1 1l5 5 5-5" fill="none" stroke="#555" stroke-width="1.4"/></svg></i></div></div>
  <div class="field" style="left:341px;top:218px"><label>Does It Run?</label><div class="select">Select<i><svg width="12" height="8" viewBox="0 0 12 8"><path d="M1 1l5 5 5-5" fill="none" stroke="#555" stroke-width="1.4"/></svg></i></div></div>
  <div class="field" style="left:651px;top:218px"><label>Title Available?</label><div class="select">Select<i><svg width="12" height="8" viewBox="0 0 12 8"><path d="M1 1l5 5 5-5" fill="none" stroke="#555" stroke-width="1.4"/></svg></i></div></div>
  <a class="btn btn-donate abs">Donate my vehicle now!</a>
  <div class="badges abs">
    <span class="badge" style="background:#f07a3a"></span>
    <span class="badge" style="background:#9aa2b0"></span>
    <span class="badge" style="background:#1c8c8c"></span>
  </div>
</form>

<h2 class="section-title abs" style="left:0;top:1172px">How to Donate</h2>
<div class="how-step" style="left:109px;top:1260px">
  <div class="how-icon" role="img" aria-label="Line icon of a form being filled with a pen"></div>
  <div class="how-num">1</div><h3>Contact Us</h3>
  <p>Call us at 1-800-555-0177 or<br>Fill out the online form</p>
</div>
<div class="how-step" style="left:450px;top:1260px">
  <div class="how-icon" role="img" aria-label="Line icon of a tow truck hook lifting a car"></div>
  <div class="how-num">2</div><h3>Schedule Pickup</h3>
  <p>Well call you today to arrange<br>a convenient pickup time for<br>your car donation.</p>
</div>
<div class="how-step" style="left:790px;top:1260px">
  <div class="how-icon" role="img" aria-label="Line icon of scissors cutting a tax tag"></div>
  <div class="how-num">3</div><h3>Tax Deduction</h3>
  <p>You receive a tax receipt and<br>vacation voucher</p>
</div>

<section class="impacts abs">
  <h2 class="section-title abs" style="left:0;top:84px">Your Car Impacts Veterans' Lives</h2>
  <div class="impact-card" style="left:110px">
    <div class="impact-photo" role="img" aria-label="Photo of a soldier with his wife and daughter outdoors" style="background:linear-gradient(135deg,#6f8a4a,#c8b79a 50%,#7da0c8)"></div>
    <h3>Help Us Reach Our Goal</h3>
    <p>Sed ut perspiciatis unde omnis is te natus error sit voluptatem accusan tium doloremque laudanti</p>
    <a>JOIN US</a>
  </div>
  <div class="impact-card" style="left:445px">
    <div class="impact-photo" role="img" aria-label="Photo of a smiling woman in a blue car holding keys" style="background:linear-gradient(135deg,#dfe6ee,#27427a 55%,#a4b3c8)"></div>
    <h3>Vision</h3>
    <p>Sed ut perspiciatis unde omnis is te natus error sit voluptatem accusan tium doloremque laudanti</p>
    <a>ABOUT US</a>
  </div>
  <div class="impact-card" style="left:780px">
    <div class="impact-photo" role="img" aria-label="Photo of many hands stacked together" style="background:linear-gradient(135deg,#8a8a8a,#d9a48c 50%,#6c6c6c)"></div>
    <h3>On The Field</h3>
    <p>Sed ut perspiciatis unde omnis is te natus error sit voluptatem accusan tium doloremque laudanti</p>
    <a>VOLUNTEER</a>
  </div>
</section>

<section class="why abs">
  <div class="why-photo abs" role="img" aria-label="Photo of a soldier in camouflage hugging a girl holding a small flag"></div>
  <h2 class="abs">Why Donate Your Car To Us</h2>
  <ul class="why-list abs">
    <li><svg width="14" height="14" viewBox="0 0 14 14"><circle cx="7" cy="7" r="7" fill="#fff"/><path d="M3.8 7.2l2.2 2.2 4.2-4.4" fill="none" stroke="#2c4fa8" stroke-width="1.8"/></svg><b>IRS 501(c)3 Approved :</b> Free 24/7 Pickup with No DMV Hassles.</li>
    <li><svg width="14" height="14" viewBox="0 0 14 14"><circle cx="7" cy="7" r="7" fill="#fff"/><path d="M3.8 7.2l2.2 2.2 4.2-4.4" fill="none" stroke="#2c4fa8" stroke-width="1.8"/></svg><b>Free Local Towing :</b> We will pick up your car donation, running or not, when it's most convenient, at home or work.</li>
    <li><svg width="14" height="14" viewBox="0 0 14 14"><circle cx="7" cy="7" r="7" fill="#fff"/><path d="M3.8 7.2l2.2 2.2 4.2-4.4" fill="none" stroke="#2c4fa8" stroke-width="1.8"/></svg><b>Income Tax Deduction :</b> We issue you an IRS tax receipt and get you the highest tax write-off possible.</li>
    <li><svg width="14" height="14" viewBox="0 0 14 14"><circle cx="7" cy="7" r="7" fill="#fff"/><path d="M3.8 7.2l2.2 2.2 4.2-4.4" fill="none" stroke="#2c4fa8" stroke-width="1.8"/></svg><b>No Paperwork Hassles :</b> We handle everything: DMV and IRS paperwork.</li>
    <li><svg width="14" height="14" viewBox="0 0 14 14"><circle cx="7" cy="7" r="7" fill="#fff"/><path d="M3.8 7.2l2.2 2.2 4.2-4.4" fill="none" stroke="#2c4fa8" stroke-width="1.8"/></svg><b>Schedule a Free Pickup :</b> Complete the form and a representative will call you to arrange a convenient time to pickup your car.</li>
  </ul>
</section>

<h2 class="section-title abs" style="left:7px;top:2942px">Frequently Questioned Answers</h2>
<div class="faq-item faq-open" style="top:3024px;height:147px">
  What types of vehicles can be donated?
  <svg width="12" height="8" viewBox="0 0 12 8" style="top:68px"><path d="M1 7l5-5 5 5" fill="none" stroke="#555" stroke-width="1.4"/></svg>
  <p>Nemo enim ipsam voluptatem quia voluptas sit aspernatur aut odit aut fugit, sed quia conse quuntur magni dolores eos qui ratione voluptat eque est, qui.</p>
</div>
<div class="faq-item" style="top:3187px;height:62px">What paperwork do I need to donate my vehicle?<svg width="12" height="8" viewBox="0 0 12 8"><path d="M1 1l5 5 5-5" fill="none" stroke="#555" stroke-width="1.4"/></svg></div>
<div class="faq-item" style="top:3262px;height:62px">Is my donated vehicle tax-deductible?<svg width="12" height="8" viewBox="0 0 12 8"><path d="M1 1l5 5 5-5" fill="none" stroke="#555" stroke-width="1.4"/></svg></div>
<div class="faq-item" style="top:3338px;height:62px">What if the vehicle is not registered in my name?<svg width="12" height="8" viewBox="0 0 12 8"><path d="M1 1l5 5 5-5" fill="none" stroke="#555" stroke-width="1.4"/></svg></div>
<div class="faq-item" style="top:3413px;height:62px">How much will I receive as a tax deduction for my vehicle?<svg width="12" height="8" viewBox="0 0 12 8"><path d="M1 1l5 5 5-5" fill="none" stroke="#555" stroke-width="1.4"/></svg></div>
<div class="faq-item" style="top:3488px;height:62px">When will I receive my tax receipt?<svg width="12" height="8" viewBox="0 0 12 8"><path d="M1 1l5 5 5-5" fill="none" stroke="#555" stroke-width="1.4"/></svg></div>
<div class="faq-item" style="top:3564px;height:62px">How do I schedule a pick up?<svg width="12" height="8" viewBox="0 0 12 8"><path d="M1 1l5 5 5-5" fill="none" stroke="#555" stroke-width="1.4"/></svg></div>

<footer class="site-footer abs">
  <div class="foot-brand abs"><span class="brand-dot"></span>Wheels for Harborline</div>
  <p class="foot-about abs">Offers support and/or financial assistance to veterans and active military personal and/or their family members who become newly blind and/or visually impaired from age-related macular degeneration, retinitis pigmentosa, glaucoma, keratoconus or diabetic retinopathy.</p>
  <div class="foot-call abs">
    Call Today To Donate
    <div class="phone"><svg width="26" height="26" viewBox="0 0 24 24"><path fill="#c50f12" d="M6.6 10.8a15 15 0 0 0 6.6 6.6l2.2-2.2c.3-.3.7-.4 1-.2 1.1.4 2.3.6 3.6.6.6 0 1 .4 1 1V20c0 .6-.4 1-1 1A17 17 0 0 1 3 4c0-.6.4-1 1-1h3.5c.6 0 1 .4 1 1 0 1.3.2 2.5.6 3.6.1.3 0 .7-.2 1z"/></svg>1-800-555-0177</div>
    Live Operators Available - 7 Days A Week
  </div>
  <div class="foot-seals abs"><span class="seal-rect"></span><span class="seal-circle"></span></div>
  <div class="quick abs">
    <h4>Quick Links</h4>
    <a>How To Donate</a><a>Why Donate</a><a>FAQ</a><a>About</a>
  </div>
  <div class="foot-rule abs"></div>
  <p class="copyright abs">Copyright ©2020. WHEELS FOR HARBORLINE. All rights reserved.</p>
  <div class="socials abs"><span class="social"></span><span class="social"></span><span class="social"></span><span class="social"></span></div>
</footer>

</body>
</html>
```